Fitness competition business needs a card design

I need a professional business card design using my logo. The card will be horizontal with rounded edges.

Target Market(s)

Female fitness competitors

Industry/Entity Type

Fitness

Contact Information for Business Card

Lise-Anne Korvath
Owner
stagevelora.com
210.555.0137
info@stagevelora.com

Font styles to use
Serif

Colors

Designer to choose colors to be used in the design.

Requirements
Must have
• On the back please add the following:
• Figure
• Bikini
• Physique
• Fitness
Nice to have
• Looking for a very sleek design, contemporary and easy to read.
Should not have
• Should not be difficult to read or be too busy

```html
<!DOCTYPE html>
<html lang="en">
<head>
<meta charset="utf-8">
<title>Stage Velora – Business Card</title>
<link href="https://fonts.googleapis.com/css2?family=Roboto+Condensed:wght@400;700&family=Open+Sans:wght@400&display=swap" rel="stylesheet">
<style>
  :root {
    --backdrop: #3b3b3b;
    --card: #1e1e1f;
    --card-edge: #2a2a2b;
    --white: #f4f4f4;
    --red: #d3211f;
    --grey: #9a9a9a;
    --emboss: #4a4a4c;
  }
  * { margin: 0; padding: 0; box-sizing: border-box; }
  html, body {
    width: 799px; height: 1200px; overflow: hidden;
    background: var(--backdrop);
  }
  .canvas {
    position: relative; width: 799px; height: 1200px;
    display: flex; flex-direction: column; align-items: center; justify-content: center; gap: 100px;
  }
  .card {
    position: relative; width: 700px; height: 400px;
    background: var(--card);
    border: 1px solid var(--card-edge);
    border-radius: 28px;
    box-shadow: 0 10px 30px rgba(0,0,0,.45);
    overflow: hidden;
  }

  /* Front */
  .front-brand {
    position: absolute; left: 0; right: 0; top: 130px;
    text-align: center;
    font-family: "Roboto Condensed", sans-serif; font-weight: 700;
    font-size: 74px; letter-spacing: 4px; color: var(--emboss);
    text-transform: uppercase;
  }
  .divisions {
    position: absolute; left: 0; right: 0; top: 272px;
    text-align: center;
    font-family: "Roboto Condensed", sans-serif; font-weight: 700;
    font-size: 21px; color: var(--white); text-transform: uppercase;
    letter-spacing: .3px;
  }
  .divisions .sep { color: var(--red); margin: 0 7px; font-weight: 400; }

  /* Back */
  .holder { position: absolute; left: 52px; top: 50px; }
  .holder-name {
    font-family: "Roboto Condensed", sans-serif; font-weight: 700;
    font-size: 28px; color: var(--red);
  }
  .holder-role {
    font-family: "Open Sans", sans-serif; font-size: 14px; color: var(--grey);
    margin-top: 2px;
  }
  .contacts {
    position: absolute; left: 52px; bottom: 50px;
    list-style: none;
    font-family: "Open Sans", sans-serif; font-size: 17px; color: var(--white);
  }
  .contacts li { display: flex; align-items: center; gap: 14px; margin-top: 8px; }
  .contacts svg { width: 20px; height: 20px; flex: none; }
  .back-brand {
    position: absolute; right: 52px; bottom: 90px;
    display: flex; align-items: center; gap: 12px;
  }
  .back-brand .dot {
    width: 22px; height: 22px; border-radius: 50%; background: var(--red);
  }
  .back-brand .name {
    font-family: "Roboto Condensed", sans-serif; font-weight: 700;
    font-size: 38px; color: var(--white); text-transform: uppercase; letter-spacing: 2px;
  }
</style>
</head>
<body>
<main class="canvas">

  <section class="card card-front">
    <div class="front-brand">Stage Velora</div>
    <div class="divisions">
      Figure<span class="sep">|</span>Bikini<span class="sep">|</span>Physique<span class="sep">|</span>Fitness
    </div>
  </section>

  <section class="card card-back">
    <div class="holder">
      <div class="holder-name">Lise-Anne Korvath</div>
      <div class="holder-role">Owner</div>
    </div>

    <ul class="contacts">
      <li>
        <svg viewBox="0 0 20 20" aria-hidden="true">
          <circle cx="10" cy="10" r="8.5" fill="none" stroke="#d3211f" stroke-width="1.6"/>
          <path d="M7 5.5l2 2-1 1.3c.6 1.4 1.7 2.5 3.1 3.1l1.3-1 2 2-1.2 1.6C9.8 14.3 5.7 10.2 5.4 6.7z" fill="#d3211f"/>
        </svg>
        210.555.0137
      </li>
      <li>
        <svg viewBox="0 0 20 20" aria-hidden="true">
          <circle cx="10" cy="10" r="8.5" fill="none" stroke="#d3211f" stroke-width="1.6"/>
          <circle cx="10" cy="10" r="4.5" fill="none" stroke="#d3211f" stroke-width="1.2"/>
          <path d="M5.5 10h9M10 5.5c-2 2.5-2 6.5 0 9M10 5.5c2 2.5 2 6.5 0 9" fill="none" stroke="#d3211f" stroke-width="1"/>
        </svg>
        www.stagevelora.com
      </li>
      <li>
        <svg viewBox="0 0 20 20" aria-hidden="true">
          <circle cx="10" cy="10" r="8.5" fill="none" stroke="#d3211f" stroke-width="1.6"/>
          <rect x="5.5" y="7" width="9" height="6.5" fill="none" stroke="#d3211f" stroke-width="1.2"/>
          <path d="M5.5 7l4.5 3.6L14.5 7" fill="none" stroke="#d3211f" stroke-width="1.2"/>
        </svg>
        info@stagevelora.com
      </li>
    </ul>

    <div class="back-brand">
      <span class="dot"></span>
      <span class="name">Stage Velora</span>
    </div>
  </section>

</main>
</body>
</html>
```